Design Product Packaging For Face Mask Brand

We need packaging designed for a new product, "Harbor Bloom Cover" a made in canada multi layer poly cotton reusable non-medical face mask for all people. The mask ties in the back behind the head.

Preference is a 4x6' flat polybag or 5x7" resealable stand up bag.

We would like to see bold easy to read colour block designs that use the colour pink. The final design should communicate a simple, high fashion, bold fun quality product.

IMG-9732 and 9733 are of the actual product.
Img_9695 and 9786 are our logos.
Vintageladyshoppinggreenmask is an image on our website.
2020-04_VK is the style of image we would like to have on the front of the packaging.
Maskonworldoff is an example of fun cute wording.

Please leave space for upc on the back of the package aswell. Open to your creativity in terms of design but colors must stay the same as brand.

Thank you all for you time and submissions.

Harbor Bloom Cover xoxo

Target Market(s)

Canada/USA civilians, non-health workers

Industry/Entity Type

Fashion

Font styles to use
Sans Serif

Colors
ffffff
feeeee
f9d9e8
eea4c8
e667a6
e34298
86cfc6
33b8a4
87cfc6

Requirements
Must have
• our logo, brand colors, upc on back
Nice to have
• Bold Font
Should not have
• Hard to read handwriting

```html
<!DOCTYPE html>
<html lang="en">
<head>
<meta charset="utf-8">
<title>Harbor Bloom Cover – Pouch Designs</title>
<link rel="stylesheet" href="https://fonts.googleapis.com/css2?family=Bebas+Neue&display=swap">
<style>
  :root {
    --page: #ffffff;
    --pink: #e88480;
    --pink-light: #ef9a95;
    --teal: #0b8584;
    --teal-bright: #16b1a8;
    --text-light: #f2f2f2;
    --text-teal: #0e6f6e;
  }
  * { margin: 0; padding: 0; box-sizing: border-box; }
  html, body {
    width: 1200px;
    height: 892px;
    overflow: hidden;
    background: var(--page);
    font-family: "Bebas Neue", "Arial Narrow", sans-serif;
  }
  .canvas {
    position: relative;
    width: 1200px;
    height: 892px;
  }
  .pouch {
    position: absolute;
    top: 43px;
    width: 520px;
    height: 805px;
  }
  .pouch--pink { left: 43px; background: var(--pink); }
  .pouch--teal { left: 624px; background: var(--teal); }

  .brand-mark {
    position: absolute;
    left: 50%;
    top: 92px;
    width: 110px;
    height: 110px;
    margin-left: -55px;
    border-radius: 50%;
  }
  .pouch--pink .brand-mark { background: var(--teal-bright); }
  .pouch--teal .brand-mark { background: var(--pink); }

  .brand-name {
    position: absolute;
    left: 0;
    right: 0;
    top: 222px;
    text-align: center;
    font-size: 48px;
    line-height: 1;
    letter-spacing: 0.5px;
  }
  .pouch--pink .brand-name { color: var(--text-light); }
  .pouch--teal .brand-name { color: var(--pink); }

  .mask-art {
    position: absolute;
    left: 65px;
    top: 372px;
    width: 400px;
    height: 322px;
    border-radius: 18px 18px 50% 50% / 18px 18px 62% 62%;
  }
  .pouch--pink .mask-art { background: linear-gradient(160deg, #1fbab1, #0ea49c); }
  .pouch--teal .mask-art { background: linear-gradient(160deg, #f0928e, #e8837f); }

  .product-title {
    position: absolute;
    left: 164px;
    top: 418px;
    font-size: 54px;
    line-height: 0.97;
    color: var(--text-light);
    font-weight: 400;
  }
  .product-tagline {
    position: absolute;
    left: 164px;
    top: 577px;
    font-size: 21px;
    line-height: 1;
  }
  .pouch--pink .product-tagline { color: var(--text-light); }
  .pouch--teal .product-tagline { color: var(--text-teal); }

  .unit-count {
    position: absolute;
    right: 26px;
    bottom: 28px;
    font-size: 31px;
    line-height: 1;
    color: var(--text-light);
  }
</style>
</head>
<body>
<main class="canvas">

  <section class="pouch pouch--pink">
    <div class="brand-mark"></div>
    <p class="brand-name">Harbor Bloom Cover</p>
    <div class="mask-art" role="img" aria-label="Illustration of a teal fabric face mask with ear loops"></div>
    <h1 class="product-title">Non-Medical<br>Protective<br>Face Mask</h1>
    <p class="product-tagline">Research &amp; evidence based<br>reusable masks for all</p>
    <p class="unit-count">1 Unit</p>
  </section>

  <section class="pouch pouch--teal">
    <div class="brand-mark"></div>
    <p class="brand-name">Harbor Bloom Cover</p>
    <div class="mask-art" role="img" aria-label="Illustration of a pink fabric face mask with ear loops"></div>
    <h2 class="product-title">Non-Medical<br>Protective<br>Face Mask</h2>
    <p class="product-tagline">Research &amp; evidence based<br>reusable masks for all</p>
    <p class="unit-count">1 Unit</p>
  </section>

</main>
</body>
</html>
```